Plakat-Design für Bauunternehmung
Zielgruppe
Wir sind eine Bauunternehmung (Meisterbetrieb und Ingenieurbüro) welche Erd- Maurer- und Betonarbeiten anbietet. Unser Fokus liegt auf Professionalität und qualitativ einwandfreie Arbeit. Wir sind teuer aber die besten in dem was wir machen. Unsere Zielgruppe liegt bei Kunden welche eine qualitativ einwandfreie Arbeit erwarten und bewusst sind dass das auch Geld kostet. Unserem Kunden ist die Geldfrage immer zweitrangig und er legt viel mehr wert auf andere Faktoren: Qualität, Zuverlässigkeit, Qualifikation, Termineinhaltung etc. Es ist selbstverständlich das die Kunden meist vermögender sind.
Aufgabenstellung
Format: 340 x 175 cm
Was muss drauf:
- Logo
- Firmendaten:
Lindmoosweg 7, 89079 Ulm
Telefon: +49 (0) 7305 - 4418273
Mobil: +49 (0) 176 - 20394857
E-Mail: mortek@beispielpost.de
- Zusätzliche Informationen: Es sollte irgendwo noch 'Bauunternehmung' stehen, es sollte etwas größer sein, unter Logo oder ähnlich, Es muss klar sein das wir eine Bauunternehmung sind. Zusätzlich dazu noch unsere Leistungen 'Neubau, Umbau, Anbau', nebeneinander oder übereinander ist euch überlassen.

```html
<!DOCTYPE html>
<html lang="de">
<head>
<meta charset="utf-8">
<title>mortek – Bauunternehmen Banner</title>
<link href="https://fonts.googleapis.com/css2?family=Poppins:wght@300;400;600;700;800&display=swap" rel="stylesheet">
<style>
  :root{
    --ink:#141414;
    --paper:#ffffff;
    --stage:#f2f2f2;
    --sky:#a9c6df;
    --brick:#b9826a;
    --grass:#6f9a4a;
    --shirt:#1c2748;
  }
  *{margin:0;padding:0;box-sizing:border-box}
  html,body{width:840px;height:1200px;overflow:hidden;background:var(--stage)}
  body{font-family:'Poppins',sans-serif;color:var(--ink);position:relative}
  .banner{position:absolute;left:30px;top:399px;width:780px;height:401px;background:var(--paper);box-shadow:0 10px 40px rgba(0,0,0,.15);overflow:hidden}
  .photo-frame{position:absolute;left:0;top:0;width:780px;height:401px}
  .brand{position:absolute;left:42px;top:44px;display:flex;align-items:flex-end;gap:7px}
  .brand-square{width:32px;height:32px;background:var(--ink)}
  .brand-text{display:flex;flex-direction:column;line-height:1}
  .brand-claim{font-size:4px;font-weight:600;letter-spacing:.2px;margin-bottom:2px}
  .brand-name{font-size:33px;font-weight:600;letter-spacing:-1px;line-height:.85}
  .headline{position:absolute;left:42px;top:104px;font-size:41px;font-weight:300;letter-spacing:-.5px;white-space:nowrap}
  .headline strong{font-weight:700}
  .tagline{position:absolute;left:42px;top:160px;font-size:22px;font-weight:700;letter-spacing:.3px}
  .services{position:absolute;left:43px;top:263px;display:flex;gap:20px}
  .service{display:flex;flex-direction:column;gap:4px}
  .service-label{font-size:12.5px;font-weight:700}
  .service-icon{width:55px;height:55px;background:var(--ink)}
  .contact{position:absolute;left:44px;top:358px;display:flex;gap:30px;font-size:7.5px;line-height:1.1}
  .contact-company{font-weight:700}
  .contact-table{display:grid;grid-template-columns:auto auto;column-gap:5px}
  .contact-table span:nth-child(even){font-weight:700}
  .website{position:absolute;right:38px;top:358px;font-size:25px;font-weight:800;letter-spacing:.5px}
</style>
</head>
<body>
<div class="banner">
  <svg class="photo-frame" viewBox="0 0 780 401" role="img" aria-label="Foto: Bauleiter mit Helm und Klemmbrett vor einem Rohbau">
    <defs>
      <linearGradient id="site" x1="0" y1="0" x2="0" y2="1">
        <stop offset="0" stop-color="var(--sky)"/>
        <stop offset=".45" stop-color="var(--brick)"/>
        <stop offset=".85" stop-color="#a07a62"/>
        <stop offset="1" stop-color="var(--grass)"/>
      </linearGradient>
      <linearGradient id="figure" x1="0" y1="0" x2="1" y2="0">
        <stop offset="0" stop-color="var(--shirt)" stop-opacity="0"/>
        <stop offset=".5" stop-color="var(--shirt)" stop-opacity=".55"/>
        <stop offset="1" stop-color="var(--shirt)" stop-opacity="0"/>
      </linearGradient>
    </defs>
    <path d="M330,33 H780 V337 H330 V202 H538 V92 H330 Z" fill="url(#site)" stroke="var(--ink)" stroke-width="2"/>
    <rect x="560" y="120" width="210" height="217" fill="url(#figure)"/>
  </svg>

  <div class="brand">
    <div class="brand-square"></div>
    <div class="brand-text">
      <span class="brand-claim">MEISTERBETRIEB &amp; INGENIEURBÜRO</span>
      <span class="brand-name">mortek</span>
    </div>
  </div>

  <h1 class="headline">IHR <strong>BAUUNTERNEHMEN</strong></h1>
  <p class="tagline">GUT. BESSER. MORTEK.</p>

  <div class="services">
    <div class="service">
      <span class="service-label">NEUBAU</span>
      <svg class="service-icon" viewBox="0 0 55 55" fill="none" stroke="#fff" stroke-width="1">
        <path d="M10,38 H40 M14,38 V26 H24 V38 M24,38 V20 H33 V38 M17,29 h4 M27,24 h3 M27,30 h3"/>
        <path d="M42,36 V16 M39,19 L42,16 L45,19"/>
      </svg>
    </div>
    <div class="service">
      <span class="service-label">UMBAU</span>
      <svg class="service-icon" viewBox="0 0 55 55" fill="none" stroke="#fff" stroke-width="1">
        <path d="M16,36 H38 M19,36 V26 H27 V36 M27,36 V21 H35 V36 M29,25 h4 M29,30 h4"/>
        <path d="M10,27 A17,17 0 0 1 40,15 M45,28 A17,17 0 0 1 15,40"/>
        <path d="M38,11 L40,15 L36,17 M17,44 L15,40 L19,38"/>
      </svg>
    </div>
    <div class="service">
      <span class="service-label">ANBAU</span>
      <svg class="service-icon" viewBox="0 0 55 55" fill="none" stroke="#fff" stroke-width="1">
        <path d="M8,37 H46 M12,37 V26 H21 V37 M21,37 V21 H30 V37 M24,25 h3 M24,30 h3"/>
        <path d="M30,28 H44 V37" stroke-dasharray="2 2"/>
        <path d="M37,30 v5 M34.5,32.5 h5"/>
      </svg>
    </div>
  </div>

  <div class="contact">
    <div class="contact-company">
      mortek GmbH<br>Lindmoosweg 7<br>89079 Ulm
    </div>
    <div class="contact-table">
      <span>Telefon</span><span>+49 (0) 7305 - 4418273</span>
      <span>Mobil</span><span>+49 (0) 176 - 20394857</span>
      <span>E-Mail</span><span>mortek@beispielpost.de</span>
    </div>
  </div>

  <p class="website">WWW.MORTEK-ULM.DE</p>
</div>
</body>
</html>
```